Business Card design for Recruiter providing Recruitment Staff Augmentation services

I need a double sided business card. I have used Zek to print cards in the past and really like their quality. I have a logo but need to change the tagline that is part of the graphic.

The tagline currently reads and Connnecting people with careers - but it should be removed.

The back should look like a notecard for writing a to do list with the first to-do Augment Recruiting Staff

```html
<!DOCTYPE html>
<html lang="en">
<head>
<meta charset="utf-8">
<title>Talent Summit – Business Card</title>
<link href="https://fonts.googleapis.com/css2?family=Open+Sans:wght@400;600;700&display=swap" rel="stylesheet">
<style>
  :root {
    --navy: #0b3f5f;
    --orange: #c8452a;
    --white: #ffffff;
    --backdrop: #e8e8e8;
    --emboss: #efefef;
    --rule: #d9dfe4;
    --ink-soft: #5a6f7e;
  }
  * { margin: 0; padding: 0; box-sizing: border-box; }
  html, body {
    width: 1200px; height: 900px; overflow: hidden;
    background: var(--backdrop);
    font-family: "Open Sans", Arial, sans-serif;
  }
  .canvas { position: relative; width: 1200px; height: 900px; }
  .card {
    position: absolute;
    background: var(--white);
    box-shadow: 0 2px 8px rgba(0,0,0,0.12);
    overflow: hidden;
  }
  .card-front { left: 78px; top: 35px; width: 587px; height: 362px; }
  .card-back  { left: 388px; top: 505px; width: 566px; height: 352px; }

  .front-bands { position: absolute; inset: 0; }
  .brand {
    position: absolute; left: 82px; top: 66px;
    display: flex; align-items: center; gap: 18px;
  }
  .brand-circle {
    width: 66px; height: 66px; border-radius: 50%;
    border: 3px solid var(--orange);
  }
  .brand-name {
    font-weight: 600; font-size: 38px; letter-spacing: 2px;
    color: var(--navy); line-height: 1;
  }
  .contact {
    position: absolute; left: 38px; top: 275px;
    color: var(--white); font-size: 15px; line-height: 21px;
    list-style: none;
  }
  .contact li { display: flex; align-items: center; gap: 8px; }
  .contact svg { width: 13px; height: 13px; fill: var(--white); }
  .holder {
    position: absolute; right: 38px; top: 274px;
    color: var(--white); font-weight: 700; font-size: 18px;
  }
  .holder .credential { font-weight: 400; font-size: 14px; }

  .back-mark {
    position: absolute; left: 110px; top: 22px;
    width: 340px; height: 306px; border-radius: 50%;
    border: 5px solid var(--emboss);
  }
  .todo {
    position: absolute; left: 48px; right: 48px; top: 34px;
    list-style: none;
  }
  .todo-title {
    font-size: 15px; font-weight: 700; letter-spacing: 2px;
    color: var(--navy); text-transform: uppercase;
    padding-bottom: 6px; border-bottom: 2px solid var(--orange);
    margin-bottom: 4px;
  }
  .todo-item {
    display: flex; align-items: center; gap: 12px;
    height: 44px; border-bottom: 1px solid var(--rule);
    font-size: 16px; color: var(--ink-soft);
  }
  .todo-box {
    width: 15px; height: 15px; flex: none;
    border: 1.5px solid var(--navy); border-radius: 2px;
  }
</style>
</head>
<body>
<main class="canvas">
  <section class="card card-front">
    <svg class="front-bands" viewBox="0 0 587 362" width="587" height="362" aria-hidden="true">
      <polygon points="0,198 402,198 383,224 0,224" fill="var(--orange)"/>
      <polygon points="0,227 384,227 416,190 587,190 587,362 0,362" fill="var(--navy)"/>
    </svg>
    <div class="brand">
      <span class="brand-circle"></span>
      <span class="brand-name">TALENT SUMMIT</span>
    </div>
    <ul class="contact">
      <li>
        <svg viewBox="0 0 16 16"><path d="M3 2h3l1.5 3.5-2 1.2a8 8 0 0 0 3.8 3.8l1.2-2L14 10v3a1 1 0 0 1-1 1A11 11 0 0 1 2 3a1 1 0 0 1 1-1z"/></svg>
        555-014-2278
      </li>
      <li>
        <svg viewBox="0 0 16 16"><path d="M1 3h14v10H1z M1 3l7 6 7-6" fill="var(--white)" stroke="var(--navy)" stroke-width="1.2"/></svg>
        dana@talentsummit.com
      </li>
    </ul>
    <p class="holder">Dana Whitfield, <span class="credential">SPHR</span></p>
  </section>

  <section class="card card-back">
    <span class="back-mark" aria-hidden="true"></span>
    <ul class="todo">
      <li class="todo-title">To Do</li>
      <li class="todo-item"><span class="todo-box"></span>Augment Recruiting Staff</li>
      <li class="todo-item"><span class="todo-box"></span></li>
      <li class="todo-item"><span class="todo-box"></span></li>
      <li class="todo-item"><span class="todo-box"></span></li>
      <li class="todo-item"><span class="todo-box"></span></li>
      <li class="todo-item"><span class="todo-box"></span></li>
    </ul>
  </section>
</main>
</body>
</html>
```